Redesign of existing site - Velbrin GmbH

Redesign of the following site.
https://www.velbrin-gmbh.example/

The colors red and green need to remain.
Topic: calendar binder

The font "FF Market Regular" should be used s well. But -- if you find a font which is similar and a bit more modern, then go with it. (see font-example.jpg)

The mainpage should have a slider with a video first. Enclosed is a screenshot of the video. (see video.jpg)

Logo also enclosed as svg. The red color might not be quit right. Please check it on your own.
For the second page this page should be used to redesign:
https://www.velbrin-gmbh.example/bindungen/ring-wire-bindung/

I am planing to use the DIVI builder. If you built this in DIVI builder and be able to send me the template or installation (Duplicator) that would be a huge advantage.
Updates

IMPORTANT:
I have received many designs in English. But I can't present them to the customer. Please convert them into German, otherwise they cannot be used.

Requirements
Must have
• Please translate designs into german if it is to be considered. How should I explain a design in english to the customer?

```html
<!DOCTYPE html>
<html lang="de">
<head>
<meta charset="utf-8">
<title>Velbrin Kalenderbindungen</title>
<link rel="stylesheet" href="https://fonts.googleapis.com/css2?family=Kaushan+Script&family=Poppins:wght@400;500;600;700&display=swap">
<style>
:root{
  --green:#62bb2f;
  --green-dark:#4f9e22;
  --red:#e0261f;
  --black:#000;
  --ink:#222;
  --muted:#555;
  --light:#f3f3f3;
  --white:#fff;
  --stats:#3a3a3d;
}
*{margin:0;padding:0;box-sizing:border-box}
html,body{width:1200px;height:4792px;overflow:hidden;background:var(--white)}
body{position:relative;font-family:"Poppins",sans-serif;color:var(--ink)}
.abs{position:absolute}
.script{font-family:"Kaushan Script",cursive;font-weight:400}

/* header */
.site-header{left:0;top:0;width:1200px;height:82px;background:var(--white)}
.brand{left:60px;top:16px;font-weight:700;font-size:40px;color:var(--green);letter-spacing:-1px;line-height:50px}
.main-nav{right:66px;top:30px;display:flex;gap:32px;font-size:13px;align-items:center}
.main-nav a{color:var(--ink);text-decoration:none}
.main-nav a.active{color:var(--green)}

/* hero */
.hero{left:0;top:82px;width:1200px;height:630px;background:linear-gradient(115deg,#2c2d30 0%,#5a5c62 40%,#b3a5a3 62%,#6b6d72 85%,#3a3b3e 100%)}
.hero-title{left:64px;top:198px;font-size:58px;line-height:72px;color:var(--white);white-space:nowrap}
.hero-title span{color:var(--green)}
.play{left:58px;top:362px;width:56px;height:56px;border-radius:50%;background:var(--red)}

/* intro */
.intro{left:0;top:712px;width:1200px;height:390px;background:var(--black)}
.intro-head{left:92px;top:78px;font-size:34px;line-height:48px;color:var(--green)}
.intro-text{left:618px;top:76px;width:482px;font-size:12.5px;line-height:24px;color:var(--white)}

.feature{top:1008px;width:334px;height:285px;background:var(--green);color:var(--white);text-align:center;padding:0 28px}
.feature .icon{width:76px;height:76px;margin:48px auto 14px;border:1px solid rgba(255,255,255,.4);display:flex;align-items:center;justify-content:center}
.feature .icon.solid{background:var(--white);border:none;margin-top:28px}
.feature h3{font-size:18px;font-weight:600;margin-bottom:10px}
.feature p{font-size:12px;line-height:21px}

/* about */
.about-photo{left:107px;top:1368px;width:488px;height:525px;border-radius:12px;background:linear-gradient(135deg,#d9d6cf,#5b5650 45%,#2e2c2a 75%,#6e8a3c)}
.about-head{left:662px;top:1392px;font-size:34px;line-height:48px;color:var(--green)}
.about-text{left:664px;top:1505px;width:432px;font-size:12.5px;line-height:22px;color:var(--muted)}
.about-text p+p{margin-top:16px}
.signature{left:656px;top:1790px;width:180px;height:75px;background:linear-gradient(90deg,rgba(60,60,170,.15),rgba(60,60,170,.05))}

/* bindings */
.bindings{left:0;top:1970px;width:1200px;height:673px;background:var(--light)}
.bindings-head{left:62px;top:72px;font-size:34px;color:var(--green)}
.bindings-sub{left:62px;top:136px;font-size:13px;color:var(--ink)}
.tile{width:190px;height:186px;background:var(--white);padding:28px 16px}
.tile svg{display:block;margin-bottom:16px}
.tile span{font-size:19px;font-weight:500;line-height:26px;color:var(--ink);display:block}
.bindings-photo{left:858px;top:197px;width:282px;height:381px;background:linear-gradient(160deg,#c7ccd2,#7f8791 50%,#d8dadd)}

/* technology */
.tech-head{left:0;top:2715px;width:1200px;text-align:center;font-size:36px;color:var(--green)}
.tech-card{top:2810px;width:345px;height:358px;border-radius:10px;overflow:hidden}
.tech-card span{position:absolute;left:24px;bottom:24px;font-size:22px;color:var(--white);font-weight:500;white-space:nowrap}
.tech-green{position:absolute;left:0;bottom:0;width:230px;height:210px;background:var(--green);border-top-right-radius:110px}
.tech-green span{position:absolute;left:28px;top:60px;bottom:auto;font-size:22px;line-height:30px}
.tech-arrow{position:absolute;left:160px;top:18px;width:36px;height:36px;border-radius:50%;border:1.5px solid var(--white);display:flex;align-items:center;justify-content:center}

/* stats */
.stats{left:0;top:3264px;width:1200px;height:372px;background:linear-gradient(120deg,#2b2b2e,var(--stats) 50%,#4a4a4d)}
.stat{top:0;width:360px;text-align:center;color:var(--white)}
.stat svg{margin-top:50px}
.stat .num{font-size:54px;font-weight:700;color:var(--green);line-height:64px;margin-top:6px;white-space:nowrap}
.stat .label{font-family:"Kaushan Script",cursive;font-size:30px;line-height:40px}
.stat .small{font-size:14px;margin-top:4px}

/* team */
.team-head{left:0;top:3705px;width:1200px;text-align:center;font-size:36px;color:var(--green)}
.member{top:3788px;width:259px}
.member .photo{width:259px;height:258px;background:linear-gradient(180deg,#f1f1f1,#cfd3d8 55%,#2e3440)}
.member .photo.light{background:linear-gradient(180deg,#f3f3f3,#d8dee6 50%,#a9c3dc)}
.member p{text-align:center;font-family:"Kaushan Script",cursive;font-size:21px;margin-top:14px;color:var(--ink)}

/* donate */
.footer-band{left:0;top:4327px;width:1200px;height:465px;background:var(--black)}
.donate{left:60px;top:4172px;width:1080px;height:314px;background:var(--green);border-radius:22px}
.calendar{left:140px;top:38px;width:246px;height:240px;background:linear-gradient(160deg,#fafafa,#e4e4e4);transform:rotate(-3deg)}
.donate h2{position:absolute;left:510px;top:56px;font-size:36px;color:var(--white);font-weight:400}
.donate p{position:absolute;left:510px;top:116px;width:470px;font-size:12.5px;line-height:22px;color:var(--white)}
.btn{position:absolute;left:510px;top:226px;width:136px;height:38px;border:1.5px solid var(--white);border-radius:20px;color:var(--white);font-size:14px;font-weight:600;display:flex;align-items:center;justify-content:center}

/* footer */
.foot-brand{left:60px;top:4522px;font-weight:700;font-size:40px;color:var(--red);letter-spacing:-1px}
.foot-about{left:60px;top:4600px;width:250px;font-size:12.5px;line-height:22px;color:var(--white)}
.social{top:4700px;width:32px;height:32px;border:1.5px solid var(--green);border-radius:50%}
.foot-col{top:4525px;color:var(--white)}
.foot-col h4{font-family:"Kaushan Script",cursive;font-weight:400;font-size:24px;color:var(--green);margin-bottom:14px}
.foot-col li{list-style:none;font-size:12.5px;line-height:22.5px}
.contact-row{display:flex;align-items:flex-start;gap:20px;font-size:12.5px;line-height:20px;margin-bottom:22px}
.copyright{left:0;top:4762px;width:1200px;text-align:center;font-size:11px;color:var(--white)}
.rule{left:60px;top:4748px;width:1080px;height:1px;background:#222}
</style>
</head>
<body>

<header class="site-header abs">
  <div class="brand abs">VELBRIN</div>
  <nav class="main-nav abs">
    <a class="active" href="#">Home</a><a href="#">Unternehmen</a><a href="#">Bindungen</a><a href="#">Exklusives</a><a href="#">Galerie</a><a href="#">Service</a><a href="#">Kontakt</a>
    <svg width="16" height="16" viewBox="0 0 16 16"><circle cx="6.5" cy="6.5" r="5" fill="none" stroke="#222" stroke-width="1.8"/><line x1="10.5" y1="10.5" x2="15" y2="15" stroke="#222" stroke-width="1.8"/></svg>
  </nav>
</header>

<section class="hero abs" role="img" aria-label="Videostandbild: bedruckte Bögen laufen durch eine Kalenderbindemaschine">
  <h1 class="hero-title abs script"><span>Velbrin</span> Kalender-<br>bindungen</h1>
  <div class="play abs"><svg width="56" height="56" viewBox="0 0 56 56"><path d="M23 18 L37 28 L23 38 Z" fill="#fff"/></svg></div>
</section>

<section class="intro abs">
  <h2 class="intro-head abs script">Service aus einer Hand –<br>Kompetenz vereint!</h2>
  <p class="intro-text abs">Velbrin – der Name steht für höchste Qualität und Erfahrung bei allen plan liegenden Kalender- und Broschürenbindungen. Seit über 50 Jahren beraten wir Kunden im In- und Ausland ideenreich in allen Fragen rund um Gestaltung und Funktion ihrer Produkte.</p>
</section>

<div class="feature abs" style="left:75px">
  <div class="icon"><svg width="46" height="46" viewBox="0 0 46 46" fill="none" stroke="#fff" stroke-width="1.6"><circle cx="23" cy="18" r="13"/><circle cx="23" cy="18" r="8"/><path d="M23 13l1.6 3.3 3.6.4-2.7 2.4.8 3.5-3.3-1.8-3.3 1.8.8-3.5-2.7-2.4 3.6-.4z"/><path d="M15 29l-4 12 5-2 3 4 4-10M31 29l4 12-5-2-3 4-4-10"/></svg></div>
  <h3>Exklusiv</h3>
  <p>Außergewöhnliche Aufgaben sind unsere Spezialität – Exklusivität ist unser Markenzeichen.</p>
</div>
<div class="feature abs" style="left:433px">
  <div class="icon solid"><svg width="50" height="50" viewBox="0 0 50 50" fill="none" stroke="#62bb2f" stroke-width="1.6"><circle cx="25" cy="12" r="5"/><circle cx="12" cy="22" r="4"/><circle cx="38" cy="22" r="4"/><path d="M17 32c0-6 4-10 8-10s8 4 8 10M5 38c0-5 3-9 7-9s7 4 7 9M31 38c0-5 3-9 7-9s7 4 7 9M3 44h44"/></svg></div>
  <h3>Unser Team</h3>
  <p>Seit über 50 Jahren beraten wir Kunden im In- und Ausland ideenreich in allen Fragen zu Gestaltung und Funktion ihrer Produkte.</p>
</div>
<div class="feature abs" style="left:791px">
  <div class="icon"><svg width="48" height="48" viewBox="0 0 48 48" fill="none" stroke="#fff" stroke-width="1.6"><rect x="6" y="6" width="28" height="34" rx="2"/><path d="M11 14h18M11 20h18M11 26h10"/><circle cx="33" cy="32" r="7"/><circle cx="33" cy="32" r="2.5"/><path d="M33 23v2M33 39v2M24 32h2M40 32h2"/></svg></div>
  <h3>Technische Infos</h3>
  <p>Wenn es ins Detail geht, helfen wir Ihnen gern. So präsentieren Sie Ihre Produkte bestmöglich.</p>
</div>

<div class="about-photo abs" role="img" aria-label="Foto: zwei Kollegen prüfen einen gedruckten Kalender am Schreibtisch"></div>
<h2 class="about-head abs script">Über uns –<br>Service aus einer Hand!</h2>
<div class="about-text abs">
  <p>Die Industriebuchbinderei Velbrin GmbH + Co. KG bietet Ihnen in ihrer Kernkompetenz „Welt der Bindungen“ individuelle und ganzheitliche Lösungen für unterschiedlichste Anforderungen. Mit viel Erfahrung und Erfindergeist beraten wir Sie gern. Unser Leistungsspektrum reicht von Planung und Produktion bis zum individuellen Versand an Ihre Kunden. Bücher, Broschüren, Tisch- und Wandkalender – Design und Funktion lassen sich perfekt verbinden.</p>
  <p>Unsere Partnerschaften ergänzen und erweitern unsere Fähigkeiten. Unser Lieferantennetz steht für technisches Know-how, Zuverlässigkeit und faire Zusammenarbeit.</p>
</div>
<div class="signature abs" role="img" aria-label="Handschriftliche Unterschrift der Geschäftsführung"></div>

<section class="bindings abs">
  <h2 class="bindings-head abs script">Die Leichtigkeit des Blätterns!</h2>
  <p class="bindings-sub abs">Unsere Kalenderbindungen und Bindungen im Überblick.</p>

  <div class="tile abs" style="left:60px;top:197px"><svg width="50" height="64" viewBox="0 0 50 64" fill="none" stroke="#62bb2f" stroke-width="1.6"><rect x="4" y="8" width="42" height="52" rx="2"/><path d="M10 4v8M17 4v8M24 4v8M31 4v8M38 4v8M11 22h28M11 30h28M11 38h28M11 46h20"/></svg><span>Ring-Wire-<br>Bindung</span></div>
  <div class="tile abs" style="left:258px;top:197px"><svg width="50" height="64" viewBox="0 0 50 64" fill="none" stroke="#62bb2f" stroke-width="1.6"><rect x="8" y="4" width="36" height="56" rx="2"/><path d="M4 10h8M4 18h8M4 26h8M4 34h8M4 42h8M4 50h8M18 14h18M18 22h18"/></svg><span>Spiral-<br>bindung</span></div>
  <div class="tile abs" style="left:457px;top:197px"><svg width="60" height="64" viewBox="0 0 60 64" fill="none" stroke="#62bb2f" stroke-width="1.6"><rect x="4" y="40" width="52" height="14" rx="3"/><rect x="8" y="26" width="46" height="14" rx="3"/><rect x="4" y="12" width="50" height="14" rx="3"/><path d="M12 19h30M14 33h30M12 47h34"/></svg><span>Leinen-<br>falz</span></div>
  <div class="tile abs" style="left:656px;top:197px"><svg width="50" height="64" viewBox="0 0 50 64" fill="none" stroke="#62bb2f" stroke-width="1.6"><path d="M25 6v52M25 6L8 12v48l17-2M25 6l17 6v48l-17-2"/><path d="M14 20h6M30 20h6"/></svg><span>Falz-<br>naht</span></div>
  <div class="tile abs" style="left:60px;top:392px"><svg width="60" height="64" viewBox="0 0 60 64" fill="none" stroke="#62bb2f" stroke-width="1.6"><rect x="8" y="6" width="40" height="52" rx="2"/><path d="M4 12h8M4 20h8M4 28h8M4 36h8M4 44h8M4 52h8"/><rect x="16" y="14" width="26" height="20"/><path d="M16 30l8-8 6 6 4-4 8 8"/><circle cx="52" cy="52" r="7" fill="#e6f3dc" stroke="none"/></svg><span>Verdeckte<br>Bindung</span></div>
  <div class="tile abs" style="left:258px;top:392px"><svg width="64" height="64" viewBox="0 0 64 64" fill="none" stroke="#62bb2f" stroke-width="1.6"><rect x="4" y="18" width="20" height="30"/><rect x="40" y="18" width="20" height="30"/><path d="M32 8v48M28 26h8v14h-8z"/></svg><span>Halbverdeckte<br>Bindung</span></div>
  <div class="tile abs" style="left:457px;top:392px"><svg width="64" height="64" viewBox="0 0 64 64" fill="none" stroke="#62bb2f" stroke-width="1.6"><path d="M6 12v40l30-20z"/><path d="M42 12v40"/><circle cx="50" cy="48" r="8" fill="#e6f3dc" stroke="none"/></svg><span>Sprung-<br>bindung</span></div>
  <div class="tile abs" style="left:656px;top:392px"><svg width="50" height="64" viewBox="0 0 50 64" fill="none" stroke="#62bb2f" stroke-width="1.6"><rect x="6" y="6" width="34" height="52" rx="2"/><path d="M12 4v6M20 4v6M28 4v6M14 22h18M14 30h18M14 38h12"/><circle cx="40" cy="52" r="7" fill="#e6f3dc" stroke="none"/></svg><span>Lose<br>Blätter</span></div>

  <div class="bindings-photo abs" role="img" aria-label="Foto: Bedienpult einer Bindemaschine in der Produktionshalle"></div>
</section>

<h2 class="tech-head abs script">Technologie</h2>
<div class="tech-card abs" style="left:60px;background:linear-gradient(170deg,#cfd2d6,#7e8086 55%,#3d3f44)" role="img" aria-label="Foto: Stationen einer Zusammentragmaschine in Reihe"><span>Zusammentragmaschine</span></div>
<div class="tech-card abs" style="left:428px;background:linear-gradient(160deg,#3b3b3b,#8c8c8c 40%,#e8e8e8 70%,#bdbdbd)" role="img" aria-label="Foto: Stapel gefalzter Papierbögen">
  <div class="tech-green"><div class="tech-arrow"><svg width="16" height="12" viewBox="0 0 16 12" fill="none" stroke="#fff" stroke-width="1.5"><path d="M1 6h13M9 1l5 5-5 5"/></svg></div><span>Falzbogen-<br>verarbeitung</span></div>
</div>
<div class="tech-card abs" style="left:795px;background:linear-gradient(170deg,#4b5258,#8f979c 45%,#2f3438)" role="img" aria-label="Foto: Maschinen einer Kalenderfertigungsstraße"><span>Kalenderstraße</span></div>

<section class="stats abs" role="img" aria-label="Hintergrundfoto: Spiralkalender auf dunklem Holz">
  <div class="stat abs" style="left:27px"><svg width="50" height="50" viewBox="0 0 50 50" fill="none" stroke="#fff" stroke-width="1.5"><circle cx="22" cy="22" r="6"/><path d="M10 44c0-8 5-13 12-13s12 5 12 13"/><path d="M36 34l6 6 6-10"/><path d="M14 6l1.5 3 3 .3-2.2 2 .6 3-2.9-1.5-2.9 1.5.6-3-2.2-2 3-.3zM25 3l1.5 3 3 .3-2.2 2 .6 3-2.9-1.5-2.9 1.5.6-3-2.2-2 3-.3zM36 6l1.5 3 3 .3-2.2 2 .6 3-2.9-1.5-2.9 1.5.6-3-2.2-2 3-.3z"/></svg><div class="num">+56</div><div class="label">Über</div><div class="small">Jahre Erfahrung</div></div>
  <div class="stat abs" style="left:419px"><svg width="50" height="50" viewBox="0 0 50 50" fill="none" stroke="#fff" stroke-width="1.5"><circle cx="22" cy="28" r="17"/><circle cx="22" cy="22" r="4"/><circle cx="13" cy="29" r="3"/><circle cx="31" cy="29" r="3"/><path d="M15 38c1-5 4-8 7-8s6 3 7 8"/><circle cx="38" cy="10" r="8"/><path d="M38 6v8M34 10h8"/></svg><div class="num">65 Mio.+</div><div class="label">Mehr als</div><div class="small">Bindungen</div></div>
  <div class="stat abs" style="left:798px"><svg width="50" height="50" viewBox="0 0 50 50" fill="none" stroke="#fff" stroke-width="1.5"><path d="M14 46V28h6l6-12c3 0 4 2 3 6l-2 6h10c3 0 4 2 3 5l-3 10c-1 2-2 3-4 3z"/><path d="M14 6l1.5 3 3 .3-2.2 2 .6 3-2.9-1.5-2.9 1.5.6-3-2.2-2 3-.3zM25 3l1.5 3 3 .3-2.2 2 .6 3-2.9-1.5-2.9 1.5.6-3-2.2-2 3-.3zM36 6l1.5 3 3 .3-2.2 2 .6 3-2.9-1.5-2.9 1.5.6-3-2.2-2 3-.3z"/></svg><div class="num">+1547</div><div class="label">Zufriedene</div><div class="small">Kunden</div></div>
</section>

<h2 class="team-head abs script">Unser Team</h2>
<div class="member abs" style="left:201px"><div class="photo" role="img" aria-label="Porträtfoto von Bernd Hallstein"></div><p>Bernd Hallstein</p></div>
<div class="member abs" style="left:490px"><div class="photo" role="img" aria-label="Porträtfoto von Jonas Wendler"></div><p>Jonas Wendler</p></div>
<div class="member abs" style="left:778px"><div class="photo light" role="img" aria-label="Porträtfoto von Carla Brenner"></div><p>Carla Brenner</p></div>

<div class="footer-band abs"></div>
<section class="donate abs">
  <div class="calendar abs" role="img" aria-label="Illustration: Wandkalender November mit Spiralbindung"></div>
  <h2 class="script">Spende an Helfende Hand</h2>
  <p>Der gemeinnützige Verein „Helfende Hand eV“ unterstützt Menschen, die Opfer von Kriminalität und Gewalt geworden sind. Dieses Anliegen liegt uns sehr am Herzen. Deshalb spenden wir an Helfende Hand eV für ein Projekt in der Region Talbrunn.</p>
  <div class="btn">Mehr lesen</div>
</section>

<div class="foot-brand abs">VELBRIN</div>
<p class="foot-about abs">Der Druckweiterverarbeiter Velbrin ist eine der größten Kalenderfabriken Deutschlands.</p>
<div class="social abs" style="left:60px"></div>
<div class="social abs" style="left:106px"></div>

<div class="foot-col abs" style="left:336px">
  <h4>Navigation</h4>
  <ul><li>Home</li><li>Unternehmen</li><li>Bindungen</li><li>Exklusives</li><li>Galerie</li><li>Service</li><li>Kontakt</li></ul>
</div>
<div class="foot-col abs" style="left:611px">
  <h4>Service</h4>
  <ul><li>Exklusiv</li><li>Unser Team</li><li>Technische Infos</li></ul>
</div>
<div class="foot-col abs" style="left:887px">
  <h4>Kontakt</h4>
  <div class="contact-row"><svg width="18" height="18" viewBox="0 0 18 18"><path d="M4 1l3 3-2 2c1 3 3 5 6 6l2-2 3 3-2 3C7 16 2 11 1 3z" fill="#62bb2f"/></svg><span>+ 0987 654 321</span></div>
  <div class="contact-row"><svg width="18" height="18" viewBox="0 0 18 18"><rect x="1" y="3" width="16" height="12" rx="1" fill="#62bb2f"/><path d="M1 4l8 6 8-6" fill="none" stroke="#000" stroke-width="1.3"/></svg><span>info@velbrin-gmbh.example</span></div>
  <div class="contact-row"><svg width="18" height="18" viewBox="0 0 18 18"><path d="M9 1a6 6 0 0 1 6 6c0 5-6 10-6 10S3 12 3 7a6 6 0 0 1 6-6z" fill="#62bb2f"/><circle cx="9" cy="7" r="2.2" fill="#000"/></svg><span>Velbrin GmbH &amp; Co. KG<br>Lindenhofweg 14<br>84999 Talbrunn</span></div>
</div>

<div class="rule abs"></div>
<p class="copyright abs">© 2025 Velbrin. Alle Rechte vorbehalten.</p>

</body>
</html>
```